Heart centered conscious skincare product maker needs mindful designer to tweak or change deodorant

Heart centered conscious skincare product maker needs mindful designer to tweak or change the roll on deodorant label (58x120mm) and design the box (40x40x108mm) it fits inside. This is a new product, I have created the label in Canva but it could use some professional eyes to tweak or change completely as appropriately convey and entice. Either way, I need a simple standing rectangle box that it will fit into with all the required (FDA) info. This product will be selling on Brindlewick so appropriate first impressions is vital. I'll have 3 more products to follow this one so the opportunity for more creative fun is available.

I will give you the final barcode soon, it is not the same one I've used on my current sample sticker.

The last attached picture of my current bottle in the grass has a thread bracelet around it that has been blessed my a balinese priest for intentions of courage, strength,love and abundance. It is our gift to our customers and is to be worn on their wrist.

Target Market(s)

USA women & men 22-54, vegan, yogis, vegetarians, organic consumers, health conscious,

Industry/Entity Type

Product

Requirements
Must have
• Professional & smart. Please show sticker design on bottle (amber bottle with black top) and with the box standing next to it at an angle and with white background.
Nice to have
• Feel free to change the colors if needed. I'm open to have white on black or black on white.. or something even more fresh like an aqua (ocean) or green (deep forest).

```html
<!DOCTYPE html>
<html lang="en">
<head>
<meta charset="utf-8">
<title>Lunara – Peppermint Deodorant Packaging</title>
<link href="https://fonts.googleapis.com/css2?family=Barlow+Condensed:wght@400;500;600;700&family=Barlow:wght@400;500&family=Lora:ital@1&display=swap" rel="stylesheet">
<style>
  :root {
    --gold: #c9962a;
    --gold-light: #dcb057;
    --gold-pale: #efdcae;
    --olive: #6b7a2f;
    --ink: #333333;
    --ink-soft: #555555;
    --paper: #ffffff;
    --backdrop: #f4f4f2;
    --rule: #b99a4f;
  }
  * { box-sizing: border-box; margin: 0; padding: 0; }
  html, body { width: 1200px; height: 1000px; overflow: hidden; }
  body {
    background: var(--backdrop);
    font-family: "Barlow", Arial, sans-serif;
    color: var(--ink);
    display: flex;
    align-items: center;
    justify-content: center;
    gap: 100px;
  }

  /* Box dieline: side + front panels */
  .box { display: flex; box-shadow: 0 2px 10px rgba(0,0,0,.08); }
  .panel {
    width: 230px; height: 620px;
    background: var(--paper);
    border-top: 10px solid var(--gold);
    border-bottom: 10px solid var(--gold);
    position: relative;
  }
  .panel + .panel { border-left: 1px solid #e6e1d6; }

  /* Side panel */
  .panel--side {
    padding: 26px 18px;
    font-family: "Barlow Condensed", "Arial Narrow", sans-serif;
    font-size: 12px;
    line-height: 1.45;
    color: var(--ink-soft);
    display: flex; flex-direction: column; gap: 16px;
  }
  .side-rule { height: 1px; background: var(--rule); width: 80%; }
  .side-heading { font-weight: 600; color: var(--ink); }
  .side-list { list-style: none; }

  /* Front panel + label shared parts */
  .panel--front, .label {
    display: flex; flex-direction: column; align-items: center;
  }
  .panel--front { padding: 40px 18px 18px; }

  .brand {
    display: flex; align-items: center; gap: 10px;
    height: 120px;
  }
  .brand-dot { width: 22px; height: 22px; border-radius: 50%; background: var(--gold); flex: none; }
  .brand-name {
    font-family: "Barlow Condensed", "Arial Narrow", sans-serif;
    font-weight: 500; font-size: 40px; letter-spacing: 5px;
    color: var(--gold);
  }

  .tagline {
    font-family: "Lora", Georgia, serif; font-style: italic;
    font-size: 11px; color: var(--ink-soft);
    white-space: nowrap;
    margin-top: 34px;
  }
  .product-name {
    font-family: "Barlow Condensed", "Arial Narrow", sans-serif;
    font-weight: 700; font-size: 38px; letter-spacing: 4px;
    color: var(--gold); line-height: 1; margin-top: 14px;
  }
  .product-row { display: flex; align-items: flex-start; width: 100%; margin-top: 4px; }
  .mineral-art {
    width: 90px; height: 64px; flex: none;
    border-radius: 6px;
    background: linear-gradient(135deg, var(--gold-pale), var(--gold-light));
  }
  .product-meta { display: flex; flex-direction: column; align-items: flex-end; flex: 1; }
  .with-mg {
    font-family: "Barlow Condensed", "Arial Narrow", sans-serif;
    font-weight: 600; font-size: 15px; color: var(--gold);
  }
  .scent {
    font-family: "Barlow Condensed", "Arial Narrow", sans-serif;
    font-weight: 500; font-size: 18px; letter-spacing: 1.5px;
    color: var(--olive); margin-top: 14px;
  }
  .olive-rule { height: 1px; background: var(--olive); width: 100%; margin-top: 14px; }

  .claims { list-style: none; width: 100%; margin-top: 10px; position: relative; }
  .panel--front .claims li {
    font-size: 13.5px; letter-spacing: 1.2px; line-height: 1.75; color: var(--ink);
  }
  .vegan-seal {
    position: absolute; right: 0; bottom: 4px;
    width: 48px; height: 48px; border-radius: 50%;
    border: 3px solid var(--olive);
  }
  .footer {
    width: 100%; margin-top: auto; padding-top: 8px;
    border-top: 1px solid var(--rule);
    display: flex; justify-content: space-between; align-items: baseline;
    font-family: "Barlow Condensed", "Arial Narrow", sans-serif;
  }
  .net-weight { font-size: 13px; color: var(--ink); }
  .web { font-size: 10px; color: var(--ink-soft); }

  /* Bottle label */
  .label {
    width: 290px; height: 600px;
    background: var(--paper);
    border-top: 12px solid var(--gold);
    border-bottom: 12px solid var(--gold);
    padding: 40px 22px 20px;
    box-shadow: 0 2px 10px rgba(0,0,0,.08);
  }
  .label .tagline { font-size: 12px; }
  .label .claims { margin-top: 10px; }
  .label .claims li { font-size: 12px; letter-spacing: .6px; line-height: 1.7; }
  .label-seal-row { width: 100%; display: flex; justify-content: flex-end; margin-top: 10px; }
  .label .vegan-seal { position: static; width: 42px; height: 42px; }
</style>
</head>
<body>

  <section class="box" aria-label="Deodorant box panels">
    <article class="panel panel--side">
      <p class="side-story">Lunara (love myself) creates the highest quality and best value of natural body care products from locally grown super food ingredients in Indonesia.</p>
      <div class="side-rule"></div>
      <div>
        <p class="side-heading">Directions:</p>
        <ol class="side-list">
          <li>1) Shake bottle</li>
          <li>2) Twist top off counter clockwise</li>
          <li>3) Apply by rolling a small amount inside the armpit</li>
          <li>4) Keep cap securely tightened when not in use.</li>
        </ol>
      </div>
      <div class="side-rule"></div>
      <p><span class="side-heading">Warning:</span> The safety of this product has not been determined. Use only as directed. If irritation occurs, rinse with warm water.</p>
      <div class="side-rule"></div>
      <p>Lunara is inspired by Balinese culture, which encourages us to nurture harmony with spirit, the environment and with one another.</p>
    </article>

    <article class="panel panel--front">
      <div class="brand">
        <span class="brand-dot"></span>
        <span class="brand-name">LUNARA</span>
      </div>
      <p class="tagline">Long Lasting 24 Hour Odor-Protection</p>
      <h1 class="product-name">DEODORANT</h1>
      <div class="product-row">
        <div class="mineral-art" role="img" aria-label="Magnesium mineral illustration"></div>
        <div class="product-meta">
          <span class="with-mg">with Magnesium</span>
          <span class="scent">PEPPERMINT</span>
        </div>
      </div>
      <div class="olive-rule"></div>
      <ul class="claims">
        <li>100% Natural &amp; Organic</li>
        <li>No Baking Soda</li>
        <li>No Synthethic Fragrance</li>
        <li>No Aluminium</li>
        <li>No Parabens</li>
        <li>No Sulfate</li>
        <li class="vegan-seal" aria-label="Vegan seal"></li>
      </ul>
      <div class="footer">
        <span class="net-weight">Net Wt. 1.69oz (50ml)</span>
        <span class="web">www.lunarabody.com</span>
      </div>
    </article>
  </section>

  <article class="label" aria-label="Bottle label">
    <div class="brand">
      <span class="brand-dot"></span>
      <span class="brand-name">LUNARA</span>
    </div>
    <p class="tagline">Long Lasting 24 Hour Odor-Protection</p>
    <h2 class="product-name">DEODORANT</h2>
    <div class="product-row">
      <div class="mineral-art" role="img" aria-label="Magnesium mineral illustration"></div>
      <div class="product-meta">
        <span class="with-mg">with Magnesium</span>
        <span class="scent">PEPPERMINT</span>
      </div>
    </div>
    <div class="olive-rule"></div>
    <ul class="claims">
      <li>100% Natural &amp; Organic · No Baking Soda</li>
      <li>No Synthethic Fragrance · No Aluminium</li>
      <li>No Parabens · No Sulfate</li>
    </ul>
    <div class="label-seal-row">
      <span class="vegan-seal" role="img" aria-label="Vegan seal"></span>
    </div>
    <div class="footer">
      <span class="net-weight">Net Wt. 1.69oz (50ml)</span>
      <span class="web">www.lunarabody.com</span>
    </div>
  </article>

</body>
</html>
```